Lottery Website Design

Full website design, where you can take part on a lottery. Inkl Logo. The website is already developed: http://www.nie-tombola.de
I like the modern fullscreen design from
http://www.zephyrdrawhall.com/en-us/home.html
but the field for using the lottery right away should be present as well an the first screen like here:
https://www.tippfalken.de/tipp/
Colour Scheme:
Red and Yellow?
Responsive design and coding (HTML & CSS).
The current website layout with bootstrap design ist http://www.nie-tombola.de - the logo may be similar to favicon
Feel free to ask! :)
As always I am looking forward for your great ideas!
Reason: Not yet the best result found ...

```html
<!DOCTYPE html>
<html lang="en">
<head>
<meta charset="utf-8">
<title>Nie Tombola (beta) – Kostenlose Lotto-Simulation</title>
<link rel="stylesheet" href="https://fonts.googleapis.com/css2?family=Open+Sans:ital,wght@0,400;0,600;0,700;0,800;1,700&family=Baloo+2:wght@700;800&display=swap">
<style>
:root{
  --red:#e2141b;
  --yellow:#fccf2f;
  --yellow-deep:#f5c21b;
  --teal:#8fcfc9;
  --teal-soft:#cfeeea;
  --ink:#333;
  --muted:#777;
  --line:#dcdcdc;
  --pink:#f6dcdc;
  --pink-ink:#e9b9b9;
  --green:#4cae4c;
  --footer:#3b3b3b;
}
*{box-sizing:border-box;margin:0;padding:0}
html,body{width:1008px;height:1200px;overflow:hidden}
body{position:relative;background:#fff;font-family:"Open Sans",Arial,sans-serif;color:var(--ink);font-size:10px}
.abs{position:absolute}

.hero-bg{position:absolute;left:0;top:0;width:1008px;height:790px;
  background:linear-gradient(180deg,var(--teal-soft) 0%,#bfe3df 35%,var(--teal) 60%,#d9f0ed 84%,#fff 100%)}
.hero-arc{position:absolute;left:0;top:0}

.topbar .contact{top:13px;font-size:12px;display:flex;align-items:center;gap:6px}
.topbar .phone{left:138px;color:#e08a1e;font-weight:600}
.topbar .mail{left:246px;color:#888;font-size:11px}
.topbar .status{left:658px;top:12px;color:#999;font-size:11px}
.btn-top{top:8px;height:21px;padding:0 10px;font-size:10px;line-height:19px;border:1px solid #ccc;border-radius:2px;background:linear-gradient(#fff,#e9e9e9);color:#333}
.btn-register{left:760px}.btn-login{left:818px;width:54px;text-align:center}

.brand-mark{left:482px;top:4px;width:44px;height:44px;border-radius:50%;background:var(--yellow)}
.brand-name{left:0;width:1008px;top:51px;text-align:center;font-size:16px;font-weight:600;color:var(--red)}
.brand-tag{left:0;width:1008px;top:73px;text-align:center;font-size:8.5px;color:#888}
.nav{left:0;width:1008px;top:106px;display:flex;justify-content:center;gap:12px;font-size:9.5px;text-transform:uppercase;color:#444}
.nav span{display:flex;align-items:center;gap:12px}
.nav span+span::before{content:"";width:3px;height:3px;border-radius:50%;background:#e08a1e}
.nav .active{color:var(--red);border-bottom:1px solid var(--red);padding-bottom:2px}

.countdown{left:136px;top:215px;width:736px;height:79px;background:linear-gradient(90deg,#f2f2f2,#fafafa);border-radius:3px;overflow:hidden}
.countdown svg{position:absolute;left:0;top:0}
.cutoff{left:26px;top:24px;font-size:19px;font-weight:700;font-style:italic;color:var(--red)}
.digits{left:118px;top:20px;display:flex;gap:8px}
.unit{display:flex;flex-direction:column;align-items:center}
.unit .nums{display:flex;gap:2px}
.unit b{width:17px;height:29px;background:#fff;border:1px solid #bbb;border-radius:2px;font:800 22px/27px "Open Sans",sans-serif;text-align:center;color:#222}
.unit small{font-size:6.5px;font-weight:700;margin-top:2px;color:#333}
.jackpot-four{left:376px;top:-6px;font:800 74px/1 "Baloo 2",sans-serif;color:var(--red)}
.jackpot-top{left:420px;top:9px;font:800 27px/1 "Baloo 2",sans-serif;color:var(--red)}
.jackpot-bottom{left:420px;top:38px;font:700 27px/1 "Baloo 2",sans-serif;color:#333}

.step{left:148px;top:322px;font-size:13px;color:#333}
.step em{color:var(--red);font-weight:700}

.play-panel{left:148px;top:356px;width:472px;height:446px;background:#fff;border:1px solid #e2e2e2}
.grid{left:13px;top:12px;display:grid;grid-template-columns:repeat(6,67px);grid-auto-rows:71px;column-gap:7.5px;row-gap:8px}
.cell{background:var(--pink);border:1px solid #f0cfcf;display:flex;align-items:center;justify-content:center;font-size:50px;color:var(--pink-ink);font-weight:400;
  background-image:linear-gradient(#fbeaea 1px,transparent 1px),linear-gradient(90deg,#fbeaea 1px,transparent 1px);background-size:6px 6px}
.options{left:0;top:172px;width:470px;height:150px;background:var(--yellow)}
.label{font-size:9.5px;font-weight:600;color:#333}
.chips{display:flex;gap:4px}
.chip{min-width:17px;height:17px;padding:0 4px;background:#fff6c8;border:1px solid #e8c94b;font-size:9px;font-weight:700;text-align:center;line-height:15px;color:#333}
.chip.on{background:var(--red);border-color:var(--red);color:#fff}
.select{position:absolute;width:126px;height:19px;background:#fff8d6;border:1px solid #e3c24a;font-size:9px;line-height:17px;padding-left:5px}
.select::after{content:"";position:absolute;right:6px;top:7px;border:4px solid transparent;border-top-color:#888}
.fine{font-size:7.5px;color:#555}
.chip.wide{width:44px}

.bottom-row{left:0;top:322px;width:470px;height:124px}
.ticket{display:flex;align-items:center;gap:4px}
.ticket-box{display:flex;gap:2px;padding:4px 5px;border:1px solid #999;border-radius:3px;background:#f4f4f4}
.ticket-box b{width:12px;height:20px;background:#fff;font-size:11px;line-height:20px;text-align:center;color:#222}
.ticket-box b.on{background:var(--red);color:#fff}
.lotto-add{position:absolute;width:76px;height:19px;background:var(--pink);border:1px solid #e4bcbc;font-size:8.5px;font-weight:700;line-height:17px;padding-left:22px;color:#333}
.lotto-add::before{content:"";position:absolute;left:7px;top:5px;width:8px;height:7px;border-radius:50%;background:#c9a3a3}
.stake-box{width:92px;height:32px;border:1px solid #ccc;font-size:15px;font-weight:700;text-align:right;padding-right:10px;line-height:30px}
.play-btn{width:92px;height:24px;background:var(--green);color:#fff;border-radius:2px;font-size:10px;font-weight:700;text-align:center;line-height:24px}

.benefits{left:640px;top:356px;width:232px}
.benefits h2{font-size:14px;font-weight:600;margin-bottom:8px}
.benefits li{list-style:none;font-size:9.5px;line-height:19px;padding-left:12px;position:relative}
.benefits li::before{content:"»";position:absolute;left:0;color:#555}

.trust{left:642px;top:511px;width:214px;height:132px;border:1px solid #ccc;background:#f7f7f7;padding:6px}
.trust .head{background:#ececec;border:1px solid #ddd;height:28px;text-align:center;font-size:11.5px;line-height:26px;color:#444}
.trust .body{background:#fff;height:82px;text-align:center;padding-top:6px}
.trust .score{font-size:14px;font-weight:700;color:#333}
.trust .rate{font-size:12px;font-weight:600;color:#555}
.trust .cta{text-align:center;font-size:11.5px;font-weight:600;color:var(--red);margin-top:-2px}

.social{left:640px;top:672px;width:212px;height:126px;border:1px solid #bbb;background:#fff}
.social .bar{background:#eceef5;border-bottom:1px solid #ccd;height:17px;font-size:8px;font-weight:700;line-height:17px;padding-left:5px;color:#333}
.social .page{position:absolute;left:6px;top:22px;font-size:10.5px;display:flex;gap:6px;align-items:center}
.social .like{font-size:7px;border:1px solid #bbb;padding:0 3px;background:#f4f4f4}
.social .count{position:absolute;left:6px;top:44px;font-size:7px;color:#555}
.social .faces{position:absolute;left:6px;top:56px;width:200px;height:32px;background:linear-gradient(90deg,#8a6f6a,#b9857d,#5b5d6e,#c44a5a,#4a4f5c)}
.social .foot{position:absolute;left:6px;bottom:4px;font-size:6.5px;color:#555}

.about{left:136px;top:832px;width:736px}
.about h1{font-size:13.5px;font-weight:700;margin-bottom:6px}
.about p{font-size:9.6px;line-height:13.8px;color:#444;margin-bottom:14px}
.about a{color:var(--red);text-decoration:none}

.footer{left:0;top:1160px;width:1008px;height:40px;background:var(--footer);color:#eee;font-size:10px;line-height:40px}
.footer .copy{position:absolute;left:136px}
.footer .links{position:absolute;right:136px}
.footer .links span{margin:0 4px}
</style>
</head>
<body>
<div class="hero-bg" role="img" aria-label="Soft teal watercolour background with light rays"></div>
<svg class="hero-arc" width="1008" height="170" viewBox="0 0 1008 170" aria-hidden="true">
  <path d="M0 0 H1008 V18 C820 30 760 150 504 158 C248 150 188 30 0 18 Z" fill="#fff"/>
</svg>

<header class="topbar">
  <div class="abs contact phone">
    <svg width="13" height="11" viewBox="0 0 13 11"><path d="M1 4 C1 1 12 1 12 4 L10 5 L9 3 H4 L3 5 Z M3 6 H10 L11 10 H2 Z" fill="#999"/></svg>
    014-555-2671
  </div>
  <div class="abs contact mail">
    <svg width="12" height="9" viewBox="0 0 12 9"><rect x=".5" y=".5" width="11" height="8" fill="none" stroke="#999"/><path d="M.5 .5 L6 5 L11.5 .5" fill="none" stroke="#999"/></svg>
    info@nie-tombola.de.au
  </div>
  <div class="abs status">You are not logged</div>
  <div class="abs btn-top btn-register">Register</div>
  <div class="abs btn-top btn-login">Login</div>

  <div class="abs brand-mark"></div>
  <div class="abs brand-name">Nie Tombola (beta)</div>
  <div class="abs brand-tag">Kostenlose Lotto-Simulation mit Kostenkontrolle</div>
  <nav class="abs nav">
    <span class="active">Home</span><span>About</span><span>How it work</span><span>Imprint</span><span>Contact us</span>
  </nav>
</header>

<section class="abs countdown">
  <svg width="736" height="79" viewBox="0 0 736 79" aria-hidden="true"><polygon points="0,0 330,0 358,39.5 330,79 0,79" fill="#fccf2f"/></svg>
  <div class="abs cutoff">Cut-off in:</div>
  <div class="abs digits">
    <div class="unit"><div class="nums"><b>3</b><b>8</b></div><small>DAYS</small></div>
    <div class="unit"><div class="nums"><b>2</b><b>3</b></div><small>HOURS</small></div>
    <div class="unit"><div class="nums"><b>5</b><b>5</b></div><small>MINUTE</small></div>
    <div class="unit"><div class="nums"><b>0</b><b>1</b></div><small>SECOND</small></div>
  </div>
  <div class="abs jackpot-four">4</div>
  <div class="abs jackpot-top">MILLION EN EUROS</div>
  <div class="abs jackpot-bottom">in lottery jackpot</div>
</section>

<p class="abs step">Step 1: Choose numbers that are to be checked for <em>Free</em> at the next draw</p>

<section class="abs play-panel">
  <div class="abs grid">
    <div class="cell">1</div><div class="cell">2</div><div class="cell">3</div><div class="cell">4</div><div class="cell">5</div><div class="cell">6</div>
    <div class="cell">7</div><div class="cell">8</div><div class="cell">9</div><div class="cell">10</div><div class="cell">11</div><div class="cell">12</div>
  </div>

  <div class="abs options">
    <div class="abs label" style="left:12px;top:18px">Quick Tips (random numbers)</div>
    <div class="abs chips" style="left:12px;top:35px"><span class="chip on">+1</span><span class="chip">+2</span><span class="chip">+3</span><span class="chip">+4</span><span class="chip">+5</span></div>

    <div class="abs label" style="left:189px;top:18px">Match Days</div>
    <div class="abs chips" style="left:189px;top:35px"><span class="chip on">Wed</span><span class="chip">Sat</span><span class="chip">Wed / Sat</span></div>

    <div class="abs label" style="left:364px;top:18px">Duration in Weeks</div>
    <div class="abs chips" style="left:364px;top:35px"><span class="chip on">1</span><span class="chip">2</span><span class="chip">3</span><span class="chip">4</span></div>

    <div class="abs label" style="left:189px;top:83px">Ziehungstag (predating)</div>
    <div class="select" style="left:189px;top:100px">Wed, 13/08/2014</div>
    <div class="abs fine" style="left:193px;top:123px">Acceptance to18:00 clock</div>

    <div class="abs label" style="left:364px;top:83px">Duration Coupon</div>
    <div class="abs chips" style="left:364px;top:100px"><span class="chip on wide">Yes</span><span class="chip wide">No</span></div>
  </div>

  <div class="abs bottom-row">
    <div class="abs label" style="left:12px;top:12px">Ticket Number</div>
    <div class="abs ticket" style="left:12px;top:32px">
      <div class="ticket-box"><b>9</b><b>0</b><b>3</b><b>4</b><b>0</b><b>0</b><b class="on">9</b></div>
      <svg width="10" height="10" viewBox="0 0 10 10"><circle cx="5" cy="5" r="3.8" fill="none" stroke="#444" stroke-width="1.4"/><path d="M5 2 V5 H7" stroke="#444" fill="none"/></svg>
    </div>

    <div class="abs label" style="left:189px;top:12px">Additional Lotteries</div>
    <div class="lotto-add" style="left:189px;top:34px">BONUS 77</div>
    <div class="lotto-add" style="left:189px;top:63px">EXTRA 6</div>
    <div class="lotto-add" style="left:189px;top:92px">PLUS 7</div>

    <div class="abs label" style="left:366px;top:12px">Stake</div>
    <div class="abs stake-box" style="left:366px;top:31px">€ 0.00</div>
    <div class="abs play-btn" style="left:366px;top:86px">Play the Lottary</div>
  </div>
</section>

<aside class="abs benefits">
  <h2>Excellent Your Benifits!</h2>
  <ul>
    <li>It's free and register</li>
    <li>Nationwide, state lottery easy and secure</li>
    <li>Save as to the applicable collection point</li>
    <li>Electronic notification of winning without frills</li>
    <li>Guaranteed payout by trustees</li>
  </ul>
</aside>

<div class="abs trust">
  <div class="head">SURE MERCHANTS</div>
  <div class="body">
    <svg width="62" height="11" viewBox="0 0 62 11" aria-hidden="true">
      <g fill="#f0a21a">
        <polygon points="5.5,0 7,4 11,4 8,6.5 9,10.5 5.5,8 2,10.5 3,6.5 0,4 4,4"/>
        <polygon transform="translate(12.5 0)" points="5.5,0 7,4 11,4 8,6.5 9,10.5 5.5,8 2,10.5 3,6.5 0,4 4,4"/>
        <polygon transform="translate(25 0)" points="5.5,0 7,4 11,4 8,6.5 9,10.5 5.5,8 2,10.5 3,6.5 0,4 4,4"/>
        <polygon transform="translate(37.5 0)" points="5.5,0 7,4 11,4 8,6.5 9,10.5 5.5,8 2,10.5 3,6.5 0,4 4,4"/>
        <polygon transform="translate(50 0)" points="5.5,0 7,4 11,4 8,6.5 9,10.5 5.5,8 2,10.5 3,6.5 0,4 4,4"/>
      </g>
    </svg>
    <div class="score">SEHRGUT</div>
    <div class="rate">4.91/5.00</div>
  </div>
  <div class="cta">Review what has been proven!</div>
</div>

<div class="abs social">
  <div class="bar">Find us on Circlenet</div>
  <div class="page">nie-tombola.de <span class="like">Like</span></div>
  <div class="count">2,994 people like</div>
  <div class="faces" role="img" aria-label="Row of member profile photos"></div>
  <div class="foot">Circlenet social plugin</div>
</div>

<article class="abs about">
  <h1>Why not a lottery?</h1>
  <p>Every week on Wednesday and Saturday are <b>the lottery numbers</b> drawn. Average 21 million German then wait for that exact their numbers are drawn from the Losfee. Nevertheless, the chance of <b>a profit</b> only 1:140 million. Six Degrees with <b>super number</b> is less likely than being hit by lightning. Even a profit, just the use of the game brings back, has a chance of not even two Prozent.Trotzdem get millions of people lottery tickets and dream of the big jackpot . Each week money in a lottery ticket to invest seems to be not a large sum, and now and then you win even a small sum which at least einspielt the current use again; maybe even something more? And then you think back to it, but even to gain significantly more.</p>
  <p>From the idea of more transparency about their own <b>lottery games</b> to get, was <b>Nie-Tombola</b> born. Here, every end of the game <a>enter his numbers</a> , he would tap on a lottery ticket and can check how much he would have won it. <b>A lottery ticket</b> is in this case <b>not filed</b> , it is merely a <a>simulation</a> . Of course, the expenses that would be associated with the delivery of a certificate will be added together, as are the sums that would have been obtained if one had actually filled out a form. This way you can tell if the lottery had paid off financially, without risking money, or at least to gain an overview of the current cost of his gambling behavior.</p>
  <p>If one uses the money you into the lottery invests play, create, otherwise, would come with time a considerable sum into being with which one could fulfill one or the other dream. Instead of hoping for a huge profit, but hardly the one will ever get, so you can focus on an actual request. Simply own lotto numbers enter , start simulation and see how much you would actually win. The results will amaze you! And just because you own in the past, large amounts of money into the lottery has set play, you must not think that a necessary investment in a future lottery win would be. The vast majority of people play their whole lives without making a significant profit. That's why prefer the numbers in our simulation and check on the money saved enjoy!</p>
</article>

<footer class="abs footer">
  <div class="copy">© Copyright 2014 nie-tombola.de</div>
  <div class="links">About Us<span>|</span>Blog<span>|</span>Contact<span>|</span>Terms and Conditions<span>|</span>Privacy Policy</div>
</footer>
</body>
</html>
```